Plakate Musikalischer Rückblick eines Italienischen Musikers
Zielgruppe
Wir brauchen ein Plakat mit dem man Veranstalter überzeugen kann Tickets in allen Altersklassen (30+) zu verkaufen.
Der Titel ist: Ventoro
Untertittel: Ein Musikalischer Rückblick eines Italienischen Musikers.
Hier ein Link zu einem Video. Das erklärt, glaube ich alles über das Projekt. https://clipvaro.net/Rk3Tm9Qp2Zs?si=Hb7NcLq4Wy81VtxA
Im Anhang sind 2 Plakate. Beide gefallen mir nicht wirklich.
Grund Plakat 1: Das Plakat ist schön aber man sieht sofort das es KI ist. Mir ist es auch ein bisschen zu viel Klischee und zu wenig Musik.
Grund Plakat 2: Ästhetisch ist es ohne Zweifel besser. Allerdings habe ich ein bisschen das Gefühl, dass es die falschen Erwartungen weckt. Ich finde die Idee gut, sich von allzu touristischen Klischees fernzuhalten. Trotzdem würde ich mir eher Dynamik und Leidenschaft wünschen, statt einer zu träumerisch-melancholischen Stimmung. Kurz gesagt: Für meinen Geschmack dürfte es ruhig etwas lebendiger sein. Die Noten sind generell OK, sehen aber nicht gut aus da dieses verblassen. Die Effekte oben, Sonne, Feuerwerk würde ich weglassen.
Aufgabenstellung
Bitte offene Datei als PS oder ID
Bitte kein KI benutzen.
Ich freue mich auf die Vorschläge

```html
<!DOCTYPE html>
<html lang="de">
<head>
<meta charset="utf-8">
<title>Ventoro – Plakat</title>
<link rel="stylesheet" href="https://fonts.googleapis.com/css2?family=Cormorant+Garamond:wght@600;700&family=Montserrat:wght@500&display=swap">
<style>
  :root {
    --page-bg: #ccc9c4;
    --sky-top: #3d416e;
    --sky-mid: #6d6791;
    --sky-rose: #8f6b8a;
    --night-bottom: #31355f;
    --title-white: #ffffff;
    --gold: #eccb3c;
    --rule-grey: #b9bccd;
    --flag-green: #2f9a4a;
    --flag-white: #f3efe9;
    --flag-red: #d12a2a;
    --town-amber: #d99a5c;
    --town-rose: #c27a78;
    --rock: #6f6166;
    --sea: #2e3858;
    --jacket: #2b3356;
    --shirt: #6f88b4;
  }
  * { margin: 0; padding: 0; box-sizing: border-box; }
  html, body {
    width: 1000px; height: 1200px; overflow: hidden;
    background: var(--page-bg);
  }
  .poster {
    position: absolute; left: 100px; top: 33px;
    width: 800px; height: 1133px; overflow: hidden;
    background: linear-gradient(180deg, var(--sky-top) 0%, var(--sky-mid) 30%, var(--sky-rose) 48%, #5a4d78 70%, var(--night-bottom) 100%);
    text-align: center;
    font-feature-settings: "lnum" 1;
    font-variant-numeric: lining-nums;
  }

  /* Bildfläche: Küstendorf, Meer und Sänger am Mikrofon */
  .hero-photo { position: absolute; left: 0; top: 350px; width: 800px; height: 720px; }
  .hero-photo .town {
    position: absolute; left: 0; top: 20px; width: 500px; height: 520px;
    background:
      radial-gradient(ellipse 260px 220px at 170px 190px, var(--town-amber) 0%, var(--town-rose) 45%, transparent 100%),
      radial-gradient(ellipse 300px 260px at 300px 360px, var(--rock) 0%, rgba(111,97,102,0.6) 55%, transparent 100%);
    filter: blur(6px);
  }
  .hero-photo .sea {
    position: absolute; left: 520px; top: 230px; width: 280px; height: 240px;
    background: linear-gradient(180deg, #3f4a6e 0%, var(--sea) 100%);
    filter: blur(8px);
  }
  .hero-photo .singer {
    position: absolute; left: 360px; top: 290px; width: 440px; height: 420px;
    background:
      radial-gradient(ellipse 60px 150px at 250px 200px, var(--shirt) 0%, transparent 100%),
      radial-gradient(ellipse 220px 260px at 260px 260px, var(--jacket) 0%, rgba(43,51,86,0.85) 60%, transparent 100%);
    filter: blur(4px);
  }
  .hero-photo .fade {
    position: absolute; left: 0; right: 0; bottom: 0; height: 280px;
    background: linear-gradient(180deg, transparent 0%, rgba(49,53,95,0.85) 55%, var(--night-bottom) 100%);
  }

  .title {
    position: absolute; left: 0; right: 0; top: 62px;
    font-family: "Cormorant Garamond", serif; font-weight: 700;
    font-size: 160px; line-height: 160px; color: var(--title-white);
    letter-spacing: 1px;
  }
  .flag-rule { position: absolute; left: 48px; top: 222px; }
  .subtitle {
    position: absolute; left: 0; right: 0; top: 248px;
    font-family: "Montserrat", sans-serif; font-weight: 500;
    font-size: 34px; line-height: 36px; color: var(--title-white);
  }
  .artist {
    position: absolute; left: 0; right: 0; top: 338px;
    font-family: "Cormorant Garamond", serif; font-weight: 700;
    font-size: 42px; line-height: 50px; letter-spacing: 1px; color: var(--gold);
  }
  .event-date {
    position: absolute; left: 0; right: 0; top: 910px;
    font-family: "Cormorant Garamond", serif; font-weight: 600;
    font-size: 76px; line-height: 76px; color: var(--gold);
  }
  .event-time {
    position: absolute; left: 0; right: 0; top: 988px;
    display: flex; align-items: center; justify-content: center; gap: 14px;
    font-family: "Cormorant Garamond", serif; font-weight: 600;
    font-size: 48px; line-height: 48px; color: var(--gold);
  }
  .event-time .rule { width: 86px; height: 3px; background: var(--rule-grey); border-radius: 2px; }
  .event-venue {
    position: absolute; left: 0; right: 0; top: 1038px;
    font-family: "Cormorant Garamond", serif; font-weight: 600;
    font-size: 68px; line-height: 68px; color: var(--gold);
  }
</style>
</head>
<body>
  <main class="poster">
    <div class="hero-photo" role="img" aria-label="Foto: der Sänger im dunklen Sakko mit geblümtem Hemd, nach oben blickend, vor einem Mikrofon am Ständer; dahinter ein farbiges Küstendorf auf Felsen am Meer in der Abenddämmerung">
      <div class="town" aria-hidden="true"></div>
      <div class="sea" aria-hidden="true"></div>
      <div class="singer" aria-hidden="true"></div>
      <div class="fade" aria-hidden="true"></div>
    </div>

    <h1 class="title">Ventoro</h1>

    <svg class="flag-rule" width="704" height="6" viewBox="0 0 704 6" aria-hidden="true">
      <defs>
        <linearGradient id="flag-line" x1="0" x2="1" y1="0" y2="0">
          <stop offset="0" stop-color="#2f9a4a" stop-opacity="0"/>
          <stop offset="0.25" stop-color="#2f9a4a"/>
          <stop offset="0.5" stop-color="#f3efe9"/>
          <stop offset="0.75" stop-color="#d12a2a"/>
          <stop offset="1" stop-color="#d12a2a" stop-opacity="0"/>
        </linearGradient>
      </defs>
      <rect x="0" y="1" width="704" height="4" rx="2" fill="url(#flag-line)"/>
    </svg>

    <p class="subtitle">Ein musikalischer Rückblick eines<br>italienischen Musikers</p>
    <p class="artist">MARCO DELVANI</p>

    <p class="event-date">XX.XX. 202X</p>
    <p class="event-time"><span class="rule"></span>00:00 UHR<span class="rule"></span></p>
    <p class="event-venue">STADT VENUE</p>
  </main>
</body>
</html>
```